First Nation Canoe Club Project

I would like to have a business card reflecting the active process of recruiting and building a canoe family

It will be more about recruiting

It will have
PLG - Tekal Canoe Journey Program
Phone: 5550198841 ext 4117
Fax:5550176620
Email: tekaladmin@brivamoteq.org
Zoom Meeting attendance scheduled through the program!
Invitations to youth and families
Invitations to caregivers and support staff

Culture * Family * Exercise * Crafts * Regalia

Song* Dance*Language*Protocol*Cooking

Laughs*Jokes*Humour*FUN!

```html
<!DOCTYPE html>
<html lang="en">
<head>
<meta charset="utf-8">
<title>PLG Tekal Canoe Journey Program – Business Card</title>
<link rel="stylesheet" href="https://fonts.googleapis.com/css2?family=Arimo:wght@400;700&display=swap">
<style>
  :root {
    --red: #e61e0a;
    --red-faint: #f0412c;
    --black: #0b0f0b;
    --white: #ffffff;
    --backdrop: #2a2a2a;
    --font: "Arimo", Arial, sans-serif;
  }
  * { box-sizing: border-box; margin: 0; padding: 0; }
  html, body { width: 1200px; height: 1015px; overflow: hidden; }
  body {
    background: var(--backdrop);
    font-family: var(--font);
    position: relative;
  }
  .card {
    position: absolute;
    left: 215px;
    width: 770px;
    height: 440px;
    overflow: hidden;
    box-shadow: 0 10px 30px rgba(0,0,0,.5);
  }
  .card--back { top: 45px; background: var(--red); }
  .card--front { top: 530px; background: var(--white); }

  /* Back: word cloud */
  .word-field {
    position: absolute; inset: -10px -20px;
    color: var(--red-faint);
    font-size: 34px; line-height: 44px;
    white-space: nowrap;
  }
  .word-field span:nth-child(3n) { font-size: 48px; }
  .word-field span:nth-child(4n) { font-size: 24px; }
  .values {
    position: absolute; left: 120px; top: 78px;
    color: var(--white);
    line-height: 1;
    white-space: nowrap;
  }
  .values p { margin-bottom: 10px; }
  .values .lg { font-size: 60px; }
  .values .md { font-size: 46px; }
  .values .sm { font-size: 34px; }
  .values .indent-1 { padding-left: 40px; }
  .values .indent-2 { padding-left: 100px; }

  /* Front */
  .front-shapes { position: absolute; inset: 0; }
  .artwork {
    position: absolute; left: 70px; top: 105px;
    width: 260px; height: 290px;
    background: var(--red);
    border-radius: 40% 40% 45% 45% / 30% 30% 60% 60%;
    border: 6px solid var(--white);
  }
  .brand {
    position: absolute; left: 380px; top: 90px;
    display: flex; align-items: center; gap: 16px;
  }
  .brand-mark {
    width: 92px; height: 92px; border-radius: 50%;
    background: var(--black);
  }
  .brand-name {
    color: var(--red); font-weight: 700; font-size: 62px; line-height: .9;
  }
  .brand-program {
    color: var(--black); font-weight: 700; font-size: 15px;
    text-transform: uppercase; line-height: 1.15; margin-top: 4px;
  }
  .contact {
    position: absolute; right: 40px;
    color: var(--white); font-size: 19px; text-align: right;
    line-height: 1.35;
  }
  .contact b { font-weight: 700; }
  .contact--band { top: 262px; }
  .contact--email { top: 370px; }
</style>
</head>
<body>

<section class="card card--back" aria-label="Card back">
  <div class="word-field" aria-hidden="true">
    <span>Culture Regalia Crafts Cooking Protocol Regalia Family Exercise FUN! Culture</span><br>
    <span>Language Culture Cooking Song Laughs Humour Jokes Family Exercise Humour</span><br>
    <span>Laughs Culture Regalia Cooking Dance Culture FUN! Family Laughs Language</span><br>
    <span>Protocol Crafts Song Cooking Humour Regalia Exercise Jokes Culture Family</span><br>
    <span>Dance Culture Cooking Language Laughs Song Humour Cooking Fam Exercise</span><br>
    <span>Regalia Culture Humour Jokes Cooking Exercise FUN! Laughs Culture Language</span><br>
    <span>Crafts Laughs Song Culture Language Humour Exercise Cooking Family Jokes</span><br>
    <span>Cooking Dance Regalia Protocol Culture FUN! Laughs Crafts Song Humour</span><br>
    <span>Culture Family Language Exercise Cooking Regalia Jokes Dance Laughs</span><br>
    <span>Humour Crafts Song Culture Cooking Language FUN! Family Protocol</span>
  </div>
  <div class="values">
    <p class="md indent-1">Culture &nbsp;<span class="lg">Family</span></p>
    <p><span class="lg">Crafts</span> <span class="sm">Regalia</span> <span class="md">Exercise</span></p>
    <p class="indent-1"><span class="sm">Song</span> <span class="md">Dance</span> <span class="sm">Language</span></p>
    <p class="indent-1"><span class="md">Laughs</span> <span class="sm">Cooking</span> <span class="md">Protocol</span></p>
    <p class="indent-2"><span class="lg">Jokes</span> <span class="sm">Humour</span> <span class="md">FUN!</span></p>
  </div>
</section>

<section class="card card--front" aria-label="Card front">
  <svg class="front-shapes" width="770" height="440" viewBox="0 0 770 440" aria-hidden="true">
    <polygon points="300,250 770,215 770,300 300,335" fill="var(--red)"/>
    <polygon points="0,330 300,335 770,300 770,440 0,440" fill="var(--black)"/>
  </svg>
  <div class="artwork" role="img" aria-label="Red formline artwork of a raised hand over a canoe paddle"></div>
  <div class="brand">
    <div class="brand-mark"></div>
    <div>
      <div class="brand-name">PLG</div>
      <div class="brand-program">Tekal Canoe<br>Journey Program</div>
    </div>
  </div>
  <div class="contact contact--band">
    <p><b>Phone:</b> 5550198841 ext 4117</p>
    <p><b>Fax:</b> 5550176620</p>
  </div>
  <div class="contact contact--email">
    <p><b>Email:</b> tekaladmin@brivamoteq.org</p>
  </div>
</section>

</body>
</html>
```